Conservative, Modern and Sharp Builder Business card

Hi there,
We would like to update our existing business card.
I have attached photos of existing business card, logo and van sign.

I would like the business card to also list what we do :
Renovation • New Build • Alteration
Extension • Bathroom • Maintenance.(Seperated by dots)

Contact number : 021 0483 0752
(With that exact spacing)

Ideally when people looking from about 2-3 metres, they know that it is a builder’s business card

Open to suggestions on fonts, layout, style of business card

PLEASE ONLY SUBMIT YOUR BEST OR MAX 3 DESIGNS FOR EACH DESIGNER

Thanks

Industry/Entity Type

Construction. Renovation

Contact Information for Business Card

Details should be the same as the existing card. And addition of what we do.

Requirements
Should not have
• The new business card must not have the same layout as our existing one. Thanks

```html
<!DOCTYPE html>
<html lang="en">
<head>
<meta charset="utf-8">
<title>StoneCrest Business Card</title>
<link rel="stylesheet" href="https://fonts.googleapis.com/css2?family=Montserrat:wght@400;500;700&display=swap">
<style>
  :root {
    --backdrop: #56595b;
    --card: #ffffff;
    --ink: #111111;
    --muted: #444648;
    --bar: #111111;
    --panel: #d4d5d7;
    --tile: #e6e7e9;
    --icon: #ffffff;
  }
  * { margin: 0; padding: 0; box-sizing: border-box; }
  html, body {
    width: 1200px; height: 1200px; overflow: hidden;
    background: var(--backdrop);
    font-family: "Montserrat", sans-serif;
    color: var(--ink);
  }
  .canvas { position: relative; width: 1200px; height: 1200px; }
  .card {
    position: absolute; left: 176px; width: 849px; height: 497px;
    background: var(--card); overflow: hidden;
  }
  .card-front { top: 74px; }
  .card-back { top: 629px; }

  .brand {
    position: absolute; font-weight: 700; letter-spacing: -0.5px;
    display: flex; align-items: center; gap: 12px; white-space: nowrap;
  }
  .brand-mark { background: var(--ink); display: inline-block; }
  .card-front .brand { left: 0; width: 445px; justify-content: center; top: 270px; font-size: 42px; }
  .card-front .brand-mark { width: 16px; height: 16px; }
  .card-back .brand { left: 430px; width: 355px; justify-content: center; top: 355px; font-size: 55px; }
  .card-back .brand-mark { width: 20px; height: 20px; }

  .holder { position: absolute; left: 455px; top: 52px; }
  .holder-name { font-size: 35px; font-weight: 700; letter-spacing: 0.3px; line-height: 1; }
  .holder-role { font-size: 20px; font-weight: 500; margin-top: 14px; letter-spacing: 0.2px; }

  .contact-bar { position: absolute; left: 445px; top: 178px; width: 34px; height: 319px; background: var(--bar); }
  .contact-panel { position: absolute; left: 479px; top: 178px; width: 370px; height: 236px; background: var(--panel); }
  .contact-list { list-style: none; position: absolute; left: 445px; top: 212px; }
  .contact-item { display: flex; align-items: center; height: 45.5px; font-size: 21px; font-weight: 500; white-space: nowrap; }
  .contact-icon { width: 34px; display: flex; justify-content: center; }
  .contact-icon svg { width: 13px; height: 13px; }
  .contact-text { margin-left: 29px; }

  .services {
    position: absolute; left: 508px; top: 432px; width: 330px;
    font-size: 14px; font-weight: 500; line-height: 1.55; color: var(--muted);
    list-style: none; white-space: nowrap;
  }

  .tile { position: absolute; background: var(--tile); }
  .tile-a { left: 0; top: 0; width: 60px; height: 59px; }
  .tile-b { left: 130px; top: 0; width: 88px; height: 59px; }
  .tile-c { left: 0; top: 117px; width: 60px; height: 88px; }
  .tile-d { left: 130px; top: 117px; width: 88px; height: 88px; }
</style>
</head>
<body>
<div class="canvas">
  <section class="card card-front">
    <div class="brand"><span class="brand-mark"></span>StoneCrest</div>

    <div class="holder">
      <h1 class="holder-name">Talen Moraine</h1>
      <p class="holder-role">Residential Builder</p>
    </div>

    <div class="contact-bar"></div>
    <div class="contact-panel"></div>
    <ul class="contact-list">
      <li class="contact-item">
        <span class="contact-icon"><svg viewBox="0 0 24 24"><path fill="var(--icon)" d="M6.6 10.8a15.2 15.2 0 0 0 6.6 6.6l2.2-2.2c.3-.3.7-.4 1-.2 1.1.4 2.3.6 3.6.6.6 0 1 .4 1 1V20c0 .6-.4 1-1 1C10.6 21 3 13.4 3 4c0-.6.4-1 1-1h3.5c.6 0 1 .4 1 1 0 1.3.2 2.5.6 3.6.1.3 0 .7-.2 1z"/></svg></span>
        <span class="contact-text">021 0483 0752</span>
      </li>
      <li class="contact-item">
        <span class="contact-icon"><svg viewBox="0 0 24 24"><rect x="2" y="5" width="20" height="14" fill="var(--icon)"/><path d="M2 5l10 8 10-8" fill="none" stroke="var(--bar)" stroke-width="2"/></svg></span>
        <span class="contact-text">StoneCrest@mailbox.com</span>
      </li>
      <li class="contact-item">
        <span class="contact-icon"><svg viewBox="0 0 24 24"><circle cx="12" cy="12" r="10" fill="none" stroke="var(--icon)" stroke-width="2.4"/><ellipse cx="12" cy="12" rx="4" ry="10" fill="none" stroke="var(--icon)" stroke-width="2"/><path d="M2 12h20" stroke="var(--icon)" stroke-width="2"/></svg></span>
        <span class="contact-text">www.<b>StoneCrest</b>.nz</span>
      </li>
      <li class="contact-item">
        <span class="contact-icon"><svg viewBox="0 0 24 24"><circle cx="12" cy="12" r="8" fill="none" stroke="var(--icon)" stroke-width="3"/></svg></span>
        <span class="contact-text">StoneCrest.nz</span>
      </li>
    </ul>

    <ul class="services">
      <li>Renovation • New Build • Alteration</li>
      <li>Extension • Bathroom • Maintenance</li>
    </ul>
  </section>

  <section class="card card-back">
    <div class="tile tile-a"></div>
    <div class="tile tile-b"></div>
    <div class="tile tile-c"></div>
    <div class="tile tile-d"></div>
    <div class="brand"><span class="brand-mark"></span>StoneCrest</div>
  </section>
</div>
</body>
</html>
```